The Hollow - Short Film Poster Design

A short film that follows a forest ranger contemplating suicide as he stumbles upon three kids lost in the forest, each in their own, different way.

Genre: Contemporary Dark Drama

Seeking a poster that really stands out as a 'Festival Piece'. See the following lists for references:

QRVN Festival Poster Awards: https://www.snapvault.example/photos/officialqrvn/with/48203917562/

Here is the FULL RESOLUTION short film to take screen grabs and reference photos from:
https://www.filecrate.example/s/kp7wq2rzt91mxe4/Hollow014.mov?oref=e

We are open to much of anything, but this project needs to stand out as unique. On top of that, we are trying to push the angle of strangers LOST in the forest (hence the name) and have thought of the opening sequence of the young man walking through the woods on the epic wide shot of being used for the poster art.

Various items need to be included on the poster: (Please feel free to reword as appropriate)

1) A FILM BY GORDON FAIRWEATHER
2) A DENNIS HOLMGRAVE PRODUCTION

All other taglines are optional and subject to addition or removal.

Please message with all other questions and comments.
Updates

Hey everyone, I apologize for not providing a high enough resolution copy of the short. I was told that this was the highest resolution until I got back straight from my editor who said it's a preliminary. Unfortunately, I do not have the ENTIRE film at top resolution. I will, however, attach high resolution .tiffs from various points of the film for use. https://www.filecrate.example/sh/wte8pqz41nd75ub/BBXKTmcPoLRWqDYe27fhZwNtb?dl=0

Industry/Entity Type

Film Production

Font styles to use
Serif
Sans Serif

Requirements
Must have
• 1) A FILM BY GORDON FAIRWEATHER
• 2) A DENNIS HOLMGRAVE PRODUCTION
• "THE HOLLOW" - Name of Film
Nice to have
• Tagline, but not necessary.

```html
<!DOCTYPE html>
<html lang="en">
<head>
<meta charset="utf-8">
<title>The Hollow — Short Film Poster</title>
<link rel="stylesheet" href="https://fonts.googleapis.com/css2?family=League+Gothic&family=Raleway:wght@500&display=swap">
<style>
  :root {
    --paper: #fbfaf7;
    --ink: #4a4a48;
    --forest-light: #b9b59a;
    --forest-mid: #7d7a55;
    --forest-deep: #4d4a34;
    --bark: #6a5a44;
  }
  html, body {
    margin: 0;
    padding: 0;
    width: 811px;
    height: 1200px;
    overflow: hidden;
    background: var(--paper);
  }
  .poster {
    position: relative;
    width: 811px;
    height: 1200px;
    background: var(--paper);
  }
  .title-art {
    position: absolute;
    inset: 0;
    width: 811px;
    height: 1200px;
  }
  .title-word {
    font-family: "League Gothic", "Oswald", sans-serif;
  }
  .credits {
    position: absolute;
    left: 0;
    right: 0;
    top: 894px;
    text-align: center;
    font-family: "Raleway", sans-serif;
    font-weight: 500;
    color: var(--ink);
    font-size: 21px;
    letter-spacing: 0.16em;
    line-height: 40px;
    margin: 0;
  }
  .credits p { margin: 0; }
</style>
</head>
<body>
<main class="poster">
  <svg class="title-art" viewBox="0 0 811 1200" role="img"
       aria-label="Title THE HOLLOW in tall condensed letters, filled with a forest photograph of a ranger in a wide-brimmed hat walking among thin trees">
    <defs>
      <linearGradient id="forest-fill" gradientUnits="userSpaceOnUse" x1="0" y1="100" x2="200" y2="860">
        <stop offset="0" stop-color="var(--forest-light)"/>
        <stop offset="0.45" stop-color="var(--forest-mid)"/>
        <stop offset="0.75" stop-color="var(--bark)"/>
        <stop offset="1" stop-color="var(--forest-deep)"/>
      </linearGradient>
    </defs>
    <text class="title-word" x="175" y="535" font-size="578"
          textLength="490" lengthAdjust="spacingAndGlyphs"
          fill="url(#forest-fill)">THE</text>
    <text class="title-word" x="0" y="851" font-size="402"
          textLength="811" lengthAdjust="spacingAndGlyphs"
          fill="url(#forest-fill)">HOLLOW</text>
  </svg>
  <div class="credits">
    <p class="credit-director">A FILM BY GORDON FAIRWEATHER</p>
    <p class="credit-producer">A DENNIS HOLMGRAVE PRODUCTION</p>
  </div>
</main>
</body>
</html>
```